Prestige Car Bodyshop Business Card

We are a car bodyshop based in the UK. Our customer base is mainly prestige high-value vehicles. I am looking for a classy and stylish business card design for my staff to give out to customers, with their direct email and phone number, as well as our main email and phone number with address details

I am also looking to have a general business card design with just our main company address and contact details, but also have a space to add a manufacturer approval logo (i.e Velmora, Orek, Tovalo etc... logo) in the corner somewhere.

I do not particularly want any outlines or pictures of cars on the card, I would just like a quality high-end look.

Please feel free to get in touch if you have any questions or queries?

Many Thanks

Malcolm

Target Market(s)

Prestige vehicle owners

Industry/Entity Type

Automotive

Contact Information for Business Card

I am looking for a classy and stylish business card design for my staff to give out to customers, with their direct email and phone number, as well as our main email and phone number with address details

Font styles to use
Sans Serif

Colors

Designer to choose colors to be used in the design.

Requirements
Nice to have
• I do not particularly want any outlines or pictures of cars on the card, I would just like a quality high-end look.

```html
<!DOCTYPE html>
<html lang="en">
<head>
<meta charset="utf-8">
<title>Halden Accident Repair Centre – Business Card</title>
<link rel="stylesheet" href="https://fonts.googleapis.com/css2?family=EB+Garamond:wght@400;700&family=Open+Sans:wght@400&display=swap">
<style>
  :root {
    --orange: #f0852b;
    --amber: #e5951a;
    --cream: #f7f1ea;
    --navy: #1d3c78;
    --brand-blue: #1f5da6;
    --ink: #111111;
    --paper: #f4f4f4;
    --photo-light: #e9e9e9;
    --photo-mid: #d2d2d2;
    --photo-dark: #b9b9b9;
  }
  * { margin: 0; padding: 0; box-sizing: border-box; }
  html, body { width: 1200px; height: 686px; overflow: hidden; background: var(--paper); }
  .card {
    position: relative;
    width: 1200px;
    height: 686px;
    overflow: hidden;
    font-family: "Open Sans", Arial, sans-serif;
    color: var(--ink);
  }
  .backdrop {
    position: absolute; inset: 0;
    background:
      radial-gradient(ellipse at 20% 75%, var(--photo-dark) 0%, transparent 55%),
      radial-gradient(ellipse at 85% 30%, var(--photo-mid) 0%, transparent 50%),
      linear-gradient(160deg, var(--photo-light) 0%, var(--photo-mid) 60%, var(--photo-light) 100%);
  }
  .corner-band { position: absolute; left: 0; top: 0; width: 480px; height: 480px; }

  .brand-dot {
    position: absolute;
    left: 29px; top: 198px;
    width: 118px; height: 118px;
    border-radius: 50%;
    background: var(--brand-blue);
  }
  .brand-name {
    position: absolute;
    left: 215px; top: 150px;
    transform: translate(-50%, -50%) rotate(-45deg);
    font-size: 40px;
    line-height: 1;
    font-weight: 400;
    color: var(--navy);
    white-space: nowrap;
  }

  .details { position: absolute; left: 520px; top: 0; }
  .row { position: absolute; left: 0; display: flex; align-items: center; white-space: nowrap; }
  .icon { width: 38px; height: 38px; flex: none; display: flex; justify-content: center; align-items: center; }
  .row .text { margin-left: 32px; }
  .person { top: 142px; }
  .person-name {
    font-family: "EB Garamond", Georgia, serif;
    font-size: 66px;
    line-height: 1;
  }
  .person-name .first { font-weight: 700; }
  .person-name .last { font-weight: 400; }
  .role {
    position: absolute; left: 70px; top: 216px;
    font-size: 32px; line-height: 1.4; white-space: nowrap;
  }
  .contact { font-size: 39px; line-height: 1.4; }
  .phone { top: 311px; }
  .email { top: 379px; }
  .address { top: 447px; align-items: flex-start; }
  .address .icon { margin-top: 12px; }
</style>
</head>
<body>
<div class="card">
  <div class="backdrop" role="img" aria-label="Faded close-up photograph of a car engine bay with wiring"></div>

  <svg class="corner-band" viewBox="0 0 480 480" aria-hidden="true">
    <polygon points="0,0 480,0 0,480" fill="var(--orange)"/>
    <polygon points="0,0 188,0 0,188" fill="var(--cream)"/>
    <polygon points="0,0 143,0 0,143" fill="var(--amber)"/>
  </svg>

  <div class="brand-dot" aria-hidden="true"></div>
  <div class="brand-name">Halden</div>

  <div class="details">
    <div class="row person">
      <span class="icon">
        <svg width="30" height="34" viewBox="0 0 30 34"><circle cx="15" cy="9" r="8" fill="var(--orange)"/><path d="M1 34 Q1 19 15 19 Q29 19 29 34 Z" fill="var(--orange)"/></svg>
      </span>
      <span class="text person-name"><span class="first">Oliver</span> <span class="last">Brandt</span></span>
    </div>
    <div class="role">Auto Electrician</div>

    <div class="row contact phone">
      <span class="icon">
        <svg width="36" height="36" viewBox="0 0 36 36"><rect width="36" height="36" rx="6" fill="var(--orange)"/><path d="M12 8 l4 5 -2 3 q2 4 6 6 l3 -2 5 4 -2 4 q-10 0 -17 -10 q-2 -5 1 -9 Z" fill="#fff"/></svg>
      </span>
      <span class="text">+ 44 20 7946 0321</span>
    </div>
    <div class="row contact email">
      <span class="icon">
        <svg width="40" height="30" viewBox="0 0 40 30"><rect width="40" height="30" rx="3" fill="var(--orange)"/><path d="M3 4 L20 17 L37 4" stroke="#fff" stroke-width="3" fill="none"/></svg>
      </span>
      <span class="text">electrician@halden.com</span>
    </div>
    <div class="row contact address">
      <span class="icon">
        <svg width="26" height="38" viewBox="0 0 26 38"><path d="M13 0 A13 13 0 0 1 26 13 Q26 22 13 38 Q0 22 0 13 A13 13 0 0 1 13 0 Z" fill="var(--orange)"/><circle cx="13" cy="13" r="5" fill="var(--paper)"/></svg>
      </span>
      <span class="text">12 Marlow Yard<br>London</span>
    </div>
  </div>
</div>
</body>
</html>
```